Business card for a gourmet fruit and vegetable retail store

Please design a business card for our boutique gourmet fruit and vegetable food store using attached logo design, with the colour options of white, black and lime green. We would like it to be unique and classic, with a large image of the logo on the back of the business card, and the business card details plus a design on the front.

Target Market(s)

High income earners in an affluent Melbourne suburb who value high quality products and done mind paying for it

Industry/Entity Type

Retail

Contact Information for Business Card

Business name: Harwick's Fine Food Merchant
Address: 27 Plumtree Rd, Kelsby VIC 3158
Name: TBC
Position Title: Director
Phone Number: TBC
Mobile: TBC

Business name is: Harwick's Fine Food Merchant. Please allow space for us to fill in the business address, contact number, person's name, position Title and mobile number.

Colors
acd036

Requirements
Must have
• The logo must have our business logo on the back, and our business details and contact details on the front. It must include the colours of white, black and lime green
Nice to have
• It can have different background colours on the front and on the back.
Should not have
• It should not have any other colours aside from white, black and lime green

```html
<!DOCTYPE html>
<html lang="en">
<head>
<meta charset="utf-8">
<title>Harwick's Fine Food Merchant – Business Card</title>
<link href="https://fonts.googleapis.com/css2?family=Roboto+Slab:wght@300;400&display=swap" rel="stylesheet">
<style>
  :root {
    --backdrop: #35302c;
    --card-black: #141414;
    --card-black-soft: #1d1d1d;
    --lime: #acd036;
    --white: #f2f2f2;
    --ghost: rgba(255, 255, 255, 0.045);
  }
  * { margin: 0; padding: 0; box-sizing: border-box; }
  html, body {
    width: 1200px;
    height: 780px;
    overflow: hidden;
    background: var(--backdrop);
    font-family: "Roboto Slab", Georgia, serif;
    color: var(--white);
  }
  .canvas {
    width: 1200px;
    height: 780px;
    display: flex;
    align-items: center;
    justify-content: center;
    gap: 40px;
  }
  .card {
    position: relative;
    width: 540px;
    height: 310px;
    background: linear-gradient(160deg, var(--card-black-soft), var(--card-black));
    overflow: hidden;
  }
  .card__band {
    position: absolute;
    left: 0;
    right: 0;
    height: 9px;
    background: var(--lime);
  }
  .card__band--top { top: 0; }
  .card__band--bottom { bottom: 0; }

  /* Back: business name */
  .brand {
    position: absolute;
    inset: 0;
    display: flex;
    align-items: center;
    justify-content: center;
  }
  .brand__name {
    font-weight: 300;
    font-size: 22px;
    letter-spacing: 0.5px;
    color: var(--white);
  }

  /* Front: contact details */
  .decor {
    position: absolute;
    left: 280px;
    top: 60px;
    width: 180px;
    height: 215px;
    border-radius: 40px;
    background: var(--ghost);
  }
  .contact {
    position: absolute;
    left: 0;
    right: 0;
    top: 70px;
  }
  .contact__name {
    font-size: 18px;
    font-weight: 400;
    letter-spacing: 1px;
    text-transform: uppercase;
    text-align: center;
    padding-left: 120px;
  }
  .contact__role {
    font-size: 14px;
    font-weight: 300;
    color: var(--lime);
    text-align: center;
    padding-left: 120px;
    margin-top: 2px;
  }
  .contact__line {
    display: flex;
    align-items: center;
    gap: 8px;
    font-size: 15px;
    font-weight: 300;
  }
  .contact__line--phone { padding-left: 90px; margin-top: 6px; }
  .contact__line--pair { justify-content: center; margin-top: 12px; }
  .contact__sep {
    width: 1.5px;
    height: 20px;
    background: var(--lime);
    margin: 0 6px;
  }
  .icon { width: 16px; height: 16px; flex: none; }
  .contact__address {
    position: absolute;
    left: 0;
    right: 0;
    bottom: 40px;
    text-align: center;
    font-size: 16px;
    font-weight: 300;
    letter-spacing: 0.5px;
  }
</style>
</head>
<body>
<main class="canvas">

  <section class="card card--back" aria-label="Card back">
    <div class="card__band card__band--top"></div>
    <div class="brand">
      <span class="brand__name">Harwick's Fine Food Merchant</span>
    </div>
    <div class="card__band card__band--bottom"></div>
  </section>

  <section class="card card--front" aria-label="Card front">
    <div class="card__band card__band--top"></div>
    <div class="decor" role="img" aria-label="Faint outline illustration of produce"></div>
    <div class="contact">
      <p class="contact__name">Daniel Marsh</p>
      <p class="contact__role">Founder</p>
      <p class="contact__line contact__line--phone">
        <svg class="icon" viewBox="0 0 16 16" aria-hidden="true"><circle cx="8" cy="8" r="7" fill="none" stroke="#acd036" stroke-width="1.4"/><rect x="5.5" y="4" width="5" height="8" rx="1" fill="none" stroke="#acd036" stroke-width="1.2"/></svg>
        <span>(03) 9555 0142</span>
      </p>
      <p class="contact__line contact__line--pair">
        <svg class="icon" viewBox="0 0 16 16" aria-hidden="true"><circle cx="8" cy="8" r="8" fill="#acd036"/><rect x="4" y="5.5" width="8" height="5.5" fill="none" stroke="#141414" stroke-width="1.1"/><path d="M4 5.5 L8 8.5 L12 5.5" fill="none" stroke="#141414" stroke-width="1.1"/></svg>
        <span>info@harwicksfood.com</span>
        <span class="contact__sep"></span>
        <svg class="icon" viewBox="0 0 16 16" aria-hidden="true"><circle cx="8" cy="8" r="8" fill="#acd036"/><path d="M5 5.5 C5 9 7 11 10.5 11 L11 9.5 L9.5 8.8 L8.8 9.5 C7.8 9 7 8.2 6.5 7.2 L7.2 6.5 L6.5 5 Z" fill="#141414"/></svg>
        <span>0400 555 318</span>
      </p>
    </div>
    <p class="contact__address">27 Plumtree Rd, Kelsby VIC 3158</p>
    <div class="card__band card__band--bottom"></div>
  </section>

</main>
</body>
</html>
```